Birch Card Flyer

Please design a flyer with all the info on attached file. We want the logo in the upper left hand corner and a very simple and clean border. We want it to come across clean and modern. Please submit one with each of the four logos you made for us. Let me know if you have any questions.

```html
<!DOCTYPE html>
<html lang="en">
<head>
<meta charset="utf-8">
<title>Birch Card Flyer</title>
<link href="https://fonts.googleapis.com/css2?family=Arimo:ital,wght@0,400;1,400&family=Questrial&display=swap" rel="stylesheet">
<style>
  :root {
    --green: #a8d58e;
    --ink: #1f1f1f;
    --grey: #58585a;
    --paper: #ffffff;
    --backdrop: #e4e5e7;
  }
  * { margin: 0; padding: 0; box-sizing: border-box; }
  html, body { width: 1200px; height: 960px; overflow: hidden; }
  body { background: var(--backdrop); position: relative; font-family: "Arimo", Arial, sans-serif; color: var(--ink); }

  .flyer {
    position: absolute; left: 480px; top: 68px; width: 664px; height: 824px;
    background: var(--paper); box-shadow: 0 2px 10px rgba(0,0,0,.15);
  }
  .brand { position: absolute; display: flex; align-items: center; gap: 10px; }
  .brand__dot { width: 16px; height: 16px; border-radius: 50%; background: var(--green); }
  .brand__name { font-family: "Questrial", sans-serif; color: var(--grey); letter-spacing: -0.5px; }
  .flyer .brand { left: 44px; top: 40px; }
  .flyer .brand__name { font-size: 34px; }

  .flyer__url-top { position: absolute; right: 66px; top: 80px; font-size: 17px; color: var(--grey); }
  .flyer__rule-top { position: absolute; left: 0; top: 124px; width: 100%; height: 7px; background: var(--green); }
  .flyer__rule-bottom { position: absolute; left: 0; top: 763px; width: 100%; height: 7px; background: var(--green); }
  .flyer__side { position: absolute; left: 0; top: 131px; width: 96px; height: 632px; background: var(--green); }
  .flyer__url-bottom { position: absolute; left: 0; width: 100%; top: 783px; text-align: center; font-size: 17px; color: var(--grey); }

  .flyer__title {
    position: absolute; left: 178px; top: 152px;
    font-family: "Questrial", sans-serif; font-weight: 400; font-size: 56px; letter-spacing: -1.5px; color: var(--grey);
  }
  .accent { color: var(--green); }

  .flyer__intro { position: absolute; left: 125px; top: 243px; width: 500px; font-size: 19px; line-height: 27.5px; }
  .flyer__intro p + p { margin-top: 26px; }

  .benefits-band {
    position: absolute; left: 96px; top: 434px; width: 448px; height: 44px;
    background: var(--green); color: var(--grey); font-size: 25px; line-height: 44px; padding-left: 30px;
  }
  .benefits { position: absolute; left: 125px; top: 510px; list-style: none; font-size: 19px; }
  .benefits li { height: 38px; line-height: 24px; padding-left: 36px; position: relative; }
  .benefits li::before { content: "*"; position: absolute; left: 0; top: -2px; }

  .card {
    position: absolute; left: 40px; top: 640px; width: 425px; height: 255px;
    background: var(--paper); box-shadow: 0 2px 10px rgba(0,0,0,.15);
  }
  .card .brand { left: 22px; top: 42px; }
  .card .brand__name { font-size: 25px; }
  .card__name { position: absolute; left: 227px; top: 105px; font-family: "Questrial", sans-serif; font-size: 23px; letter-spacing: -0.5px; color: var(--grey); }
  .card__role { position: absolute; left: 227px; top: 133px; font-size: 14px; color: var(--grey); }
  .card__contacts { position: absolute; left: 227px; top: 167px; list-style: none; font-size: 11.5px; font-style: italic; color: var(--grey); }
  .card__contacts li { height: 25px; display: flex; }
  .card__contacts .label { color: var(--green); width: 24px; }
</style>
</head>
<body>
  <article class="flyer">
    <div class="brand"><span class="brand__dot"></span><span class="brand__name">BIRCH</span></div>
    <div class="flyer__url-top">WWW.BIRCHCARDUSA.COM</div>
    <div class="flyer__rule-top"></div>
    <div class="flyer__side"></div>

    <h1 class="flyer__title">THE <span class="accent">BIRCH</span> CARD</h1>

    <div class="flyer__intro">
      <p>The Birch Card is Orange County’s exclusive Restaurant Loyalty Program.</p>
      <p>We offer a unique marketing strategy, a strategy that will help you gain new customers, increase traffic into your restaurant and solidify a loyal customer base.</p>
    </div>

    <h2 class="benefits-band" style="font-weight:400">How The Birch Card benefits you</h2>
    <ul class="benefits">
      <li>No Cost to your Restaurant</li>
      <li>Fill your tables with quality customers</li>
      <li>Free marketing and website exposure</li>
      <li>Gain new customers and solidify customer loyalty</li>
      <li>Increase traffic during your quiet periods</li>
      <li>Custom tailor options to fit your restaurants needs</li>
    </ul>

    <div class="flyer__rule-bottom"></div>
    <div class="flyer__url-bottom">WWW.BIRCHCARDUSA.COM</div>
  </article>

  <article class="card">
    <div class="brand"><span class="brand__dot"></span><span class="brand__name">The Birch Card</span></div>
    <div class="card__name">Owen Harlow</div>
    <div class="card__role">Founder</div>
    <ul class="card__contacts">
      <li><span class="label">T</span>949-555-0142</li>
      <li><span class="label">E</span>owenharlow@birchcardusa.com</li>
      <li><span class="label">W</span>www.birchcardusa.com</li>
    </ul>
  </article>
</body>
</html>
```